Biodegradable box for eco-friendly bamboo cotton buds

I am looking for a design on a box holding 200 bamboo cotton buds. The box opens like a matchstick box and is made from recycled card. It's to sell online and at markets, maybe also supermarkets.
It's the second product my company, Verdalin, will sell, so I would like a design that I can replicate on other product packaging in the future.
You can see more about Verdalin on my website www.verdalin.org or facebook and instagram @verdalinqatar.
Please see below the box dimensions from the supplier and a photo. Also, some ideas I have had using Canva. I would like to see the green strip go all the way round the box. I like the font. The cotton bud logo is copyrighted - I like the style, but a new one would need to be created.

Target Market(s)

Eco-conscious consumers - expats and locals - in Qatar

Industry/Entity Type

Retail

Font styles to use
Other font styles liked:
• special elite

Colors
cadf82
acd037
eaf2ce
9ccb3b

Requirements
Must have
• an environmentally-friendly focus

```html
<!DOCTYPE html>
<html lang="en">
<head>
<meta charset="utf-8">
<title>Verdalin bamboo cotton buds box</title>
<link rel="stylesheet" href="https://fonts.googleapis.com/css2?family=Special+Elite&family=Montserrat:wght@400;500&display=swap">
<style>
  :root {
    --bg: #ffffff;
    --panel: #eaf2ce;
    --panel-edge: #d6e4a8;
    --lime: #acd037;
    --lime-soft: #cadf82;
    --lime-deep: #9ccb3b;
    --ink: #8fb83a;
    --ink-dark: #7a9e2c;
    --white: #ffffff;
  }
  * { box-sizing: border-box; margin: 0; padding: 0; }
  html, body { width: 675px; height: 1200px; overflow: hidden; background: var(--bg); }
  .canvas { position: relative; width: 675px; height: 1200px; }
  .dieline { position: absolute; left: 64px; top: 298px; width: 546px; height: 603px; }
  .panel { position: absolute; background: var(--panel); border: 1px solid var(--panel-edge); }
  .panel--top { left: 0; top: 0; width: 325px; height: 177px; }
  .panel--front { left: 0; top: 177px; width: 325px; height: 426px; overflow: hidden; }
  .panel--side { left: 325px; top: 177px; width: 221px; height: 426px; }

  .brand { display: flex; align-items: center; gap: 8px; font-family: "Montserrat", sans-serif; font-weight: 500; color: var(--white); }
  .brand__dot { width: 12px; height: 12px; border-radius: 50%; background: var(--white); }
  .panel--top .brand { position: absolute; left: 34px; top: 28px; font-size: 18px; }

  .contact { position: absolute; left: 34px; top: 116px; font-family: "Montserrat", sans-serif; color: var(--ink-dark); font-size: 11px; line-height: 1.6; }
  .contact__social { display: flex; align-items: center; gap: 6px; }
  .contact__square { width: 11px; height: 11px; border: 1.5px solid var(--ink-dark); border-radius: 2px; }

  .title { position: absolute; left: 34px; top: 58px; font-family: "Special Elite", monospace; color: var(--ink-dark); line-height: 1; }
  .title__main { font-size: 40px; color: var(--lime-deep); }
  .title__sub { font-size: 21px; margin-top: 2px; }

  .buds-art { position: absolute; left: 34px; top: 148px; width: 270px; height: 150px; border-radius: 6px;
    background: linear-gradient(115deg, var(--lime-soft), var(--lime)); opacity: .8; }

  .band { position: absolute; top: 213px; height: 26px; background: var(--lime); }
  .band--front { left: 230px; width: 95px; }
  .band--side { left: 325px; width: 221px; display: flex; align-items: center; }
  .band__count { margin-left: 12px; font-family: "Montserrat", sans-serif; font-size: 11px; color: var(--white); }

  .brand-tab { position: absolute; left: 0; bottom: 0; width: 130px; height: 96px; background: var(--lime);
    border-top-right-radius: 48px; display: flex; align-items: center; padding-left: 16px; }
  .brand-tab .brand { font-size: 16px; }
</style>
</head>
<body>
<main class="canvas">
  <section class="dieline">
    <div class="panel panel--top">
      <div class="brand"><span class="brand__dot"></span>Verdalin</div>
      <div class="contact">
        <p>Find more products at www.verdalin.org</p>
        <p class="contact__social"><span class="contact__square"></span>@verdalinqatar</p>
      </div>
    </div>

    <div class="panel panel--front">
      <h1 class="title">
        <span class="title__main">bamboo</span><br>
        <span class="title__sub">cotton buds</span>
      </h1>
      <div class="buds-art" role="img" aria-label="Illustration of a row of bamboo cotton buds fanning out diagonally"></div>
      <div class="brand-tab">
        <div class="brand"><span class="brand__dot"></span>Verdalin</div>
      </div>
    </div>

    <div class="panel panel--side"></div>

    <div class="band band--front"></div>
    <div class="band band--side"><span class="band__count">200</span></div>
  </section>
</main>
</body>
</html>
```